Wrenfield Cattle Website

I need a website for my cattle company. I will be sharing pictures of my herd along with selling my calves individually. I need the following pages:
About
Cattle Sales
Bulls
Cows/Heifers
Gallery
Contact Us

I just uploaded a few pictures, but I have a lot more!

```html
<!DOCTYPE html>
<html lang="en">
<head>
<meta charset="utf-8">
<title>Wrenfield Cattle</title>
<link href="https://fonts.googleapis.com/css2?family=Alfa+Slab+One&family=Oswald:wght@400;500&family=Arimo:wght@400&display=swap" rel="stylesheet">
<style>
:root{
  --brown:#55402a;
  --brown-dark:#3f2f1f;
  --sage:#e6e8dc;
  --gold:#a8914f;
  --white:#ffffff;
  --text:#4a3a2a;
}
*{margin:0;padding:0;box-sizing:border-box}
html,body{width:1200px;height:5286px;overflow:hidden;background:var(--white)}
body{position:relative;font-family:'Arimo',Arial,sans-serif;color:var(--text)}
.abs{position:absolute}
.display{font-family:'Alfa Slab One',Georgia,serif;color:var(--brown);letter-spacing:1px}
.cond{font-family:'Oswald',Arial,sans-serif;text-transform:uppercase}
.btn{position:absolute;display:flex;align-items:center;justify-content:center;background:var(--brown);color:var(--white);font-family:'Oswald',Arial,sans-serif;font-size:16px;text-transform:uppercase}
.divider{position:absolute;height:10px}
.center{left:0;width:1200px;text-align:center}

/* header */
.site-header{top:0;left:0;width:1200px;height:135px;background:var(--white);z-index:3}
.logo-disc{left:90px;top:-10px;width:205px;height:210px;border-radius:50%;background:var(--white);z-index:4;display:flex;flex-direction:column;align-items:center;justify-content:center}
.logo-disc .name{font-family:'Oswald',Arial,sans-serif;font-weight:500;font-size:25px;color:var(--brown);line-height:1.05;text-align:center}
.logo-disc .place{font-family:'Oswald',Arial,sans-serif;font-weight:500;font-size:11px;color:var(--brown);margin-top:4px}
.sale-call{left:660px;top:28px;font-size:16px;color:var(--brown);display:flex;gap:8px;align-items:center}
.bid-btn{left:893px;top:18px;width:188px;height:42px;border:2px solid var(--brown);color:var(--brown);font-family:'Oswald',Arial,sans-serif;font-size:15px;display:flex;align-items:center;justify-content:center;text-transform:uppercase}
.nav a{position:absolute;top:84px;font-family:'Oswald',Arial,sans-serif;font-size:17px;color:var(--brown-dark);text-decoration:none;text-transform:uppercase}

/* hero */
.hero{top:135px;left:0;width:1200px;height:600px;background:linear-gradient(100deg,#8a9668 0%,#6f7d55 35%,#3c3a2c 62%,#6e7a52 82%,#8e9a6c 100%)}
.hero-title{left:129px;top:350px;font-family:'Alfa Slab One',Georgia,serif;font-size:58px;line-height:76px;color:var(--white);letter-spacing:2px}
.hero-btn{left:129px;top:521px;width:162px;height:56px;background:var(--brown);border:2px solid #d9cdb8}
.dots span{position:absolute;top:693px;width:14px;height:14px;border:2px solid var(--white);border-radius:50%}

/* about */
.about{top:735px;left:0;width:1200px;height:572px;background:var(--sage)}
.art-about{left:123px;top:759px;width:455px;height:493px;background:radial-gradient(ellipse at 55% 55%,#6b5233 0%,#8a6d48 45%,rgba(230,232,220,0) 72%)}
.about h2{left:650px;top:826px;font-size:50px}
.about-text{left:650px;top:932px;width:460px;font-size:22px;line-height:30.5px;color:#3a2e22}

/* sales */
.sales-title{top:1400px;font-size:50px}
.card{position:absolute;top:1543px;width:302px;height:534px;border:2px solid #8a6f52;border-radius:151px 151px 0 0;background:var(--white)}
.card .photo{position:absolute;left:-2px;top:-2px;width:302px;height:302px;border-radius:50%}
.card h3{position:absolute;top:326px;width:100%;text-align:center;font-family:'Oswald',Arial,sans-serif;font-weight:400;font-size:23px;color:var(--brown-dark);text-transform:uppercase}
.card p{position:absolute;top:375px;left:14px;right:14px;text-align:center;font-size:14.5px;line-height:20px;color:#4a4038}
.card .btn{left:94px;top:466px;width:110px;height:36px;font-size:13px}
.sdots span{position:absolute;top:2133px;width:12px;height:12px;background:var(--brown-dark);border-radius:50%}

/* bulls */
.bulls{top:2278px;left:0;width:1200px;height:605px;background:var(--gold)}
.bulls-box{left:127px;top:2395px;width:944px;height:379px;border:2px solid #efe8d4}
.bulls-photo{left:601px;top:2395px;width:470px;height:379px;background:linear-gradient(160deg,#7f9a5a 0%,#2a2620 45%,#1e1c18 70%,#6e8a4e 100%)}
.bulls h2{left:170px;top:2436px;font-size:52px;color:var(--white)}
.bulls-text{left:170px;top:2516px;width:400px;font-size:22px;line-height:30.5px;color:var(--white)}
.outline-btn{left:170px;top:2667px;width:134px;height:52px;border:2px solid #efe8d4;color:var(--white);font-family:'Oswald',Arial,sans-serif;font-size:16px;display:flex;align-items:center;justify-content:center;text-transform:uppercase}

/* cows */
.cows{top:2883px;left:0;width:1200px;height:297px;background:linear-gradient(#eef1f7,#fbfbfd)}
.cows h2{top:2958px;font-size:50px}
.cows-text{top:3046px;font-size:22px;line-height:31px;color:#3a2e22}
.cows-photo{top:3180px;left:0;width:1200px;height:298px;background:linear-gradient(#dfe1d8 0%,#b9a88a 30%,#8c6c4c 60%,#c7b592 100%)}

/* gallery */
.gallery{top:3478px;left:0;width:1200px;height:1026px;background:var(--sage)}
.gallery h2{top:3562px;font-size:50px}
.gallery-text{top:3670px;font-size:22px;line-height:31px;color:#3a2e22}
.g{position:absolute}

/* footer */
.foot-h{font-family:'Oswald',Arial,sans-serif;font-weight:500;font-size:25px;color:var(--brown-dark);letter-spacing:2px}
.foot-links a{position:absolute;left:226px;font-family:'Oswald',Arial,sans-serif;font-size:17px;color:var(--brown-dark);text-decoration:none;text-transform:uppercase}
.contact-item{position:absolute;left:841px;display:flex;gap:12px;font-family:'Oswald',Arial,sans-serif;font-size:17px;line-height:21px;color:var(--brown-dark);text-transform:uppercase}
.social span{position:absolute;top:4889px;width:31px;height:31px;border-radius:50%;background:var(--brown-dark)}
.copyright{top:4944px;font-size:16px;color:var(--brown)}
.foot-photo{top:4966px;left:0;width:1200px;height:320px;background:linear-gradient(#ffffff 0%,#dcdcd0 30%,#a3a27a 60%,#7a6a48 100%)}
</style>
</head>
<body>

<header class="abs site-header">
  <div class="abs sale-call cond">
    <svg width="18" height="18" viewBox="0 0 24 24"><path fill="#55402a" d="M6.6 10.8a15.2 15.2 0 0 0 6.6 6.6l2.2-2.2a1 1 0 0 1 1-.25 11.4 11.4 0 0 0 3.6.57 1 1 0 0 1 1 1V20a1 1 0 0 1-1 1A17 17 0 0 1 3 4a1 1 0 0 1 1-1h3.5a1 1 0 0 1 1 1c0 1.25.2 2.45.57 3.6a1 1 0 0 1-.25 1z"/></svg>
    For sale call: 55 0100 2741
  </div>
  <div class="abs bid-btn">Register to bid online</div>
  <nav class="nav">
    <a style="left:380px">About</a>
    <a style="left:482px">Cattle Sales</a>
    <a style="left:632px">Bulls</a>
    <a style="left:733px">Cows/Heifers</a>
    <a style="left:897px">Gallery</a>
    <a style="left:1014px">Contact Us</a>
  </nav>
</header>
<div class="abs logo-disc"><div class="name">WRENFIELD<br>CATTLE</div><div class="place">HARLOW CREEK, CA</div></div>

<section class="abs hero" role="img" aria-label="Highland cow with long horns standing in a wet green pasture"></section>
<h1 class="abs hero-title">WELCOME TO<br>WRENFIELD CATTLE</h1>
<div class="btn hero-btn">Read More</div>
<div class="dots"><span style="left:567px"></span><span style="left:590px"></span><span style="left:613px"></span></div>

<section class="abs about"></section>
<div class="abs art-about" role="img" aria-label="Illustration of a highland cow and calf standing on a grassy mound"></div>
<div class="about"><h2 class="abs display">ABOUT US</h2></div>
<svg class="divider" style="left:650px;top:894px" width="183" height="10"><line x1="0" y1="5" x2="183" y2="5" stroke="#55402a" stroke-width="2"/></svg>
<p class="abs about-text">Lorem ipsum dolor sit amet, consectetur adipiscing elit, sed do eiusmod tempor incididunt ut labore et dolore magna aliqua. Quis ipsum suspendisse ultrices gravida. Risus commodo viverra maecenas accumsan lacus vel facilisis.</p>
<div class="btn" style="left:644px;top:1145px;width:115px;height:45px">Read More</div>

<h2 class="abs display center sales-title">CATTLE SALES</h2>
<svg class="divider" style="left:508px;top:1472px" width="184" height="10"><line x1="0" y1="5" x2="184" y2="5" stroke="#55402a" stroke-width="2"/></svg>

<article class="card" style="left:127px">
  <div class="photo" role="img" aria-label="Red highland calf grazing in tall grass" style="background:linear-gradient(150deg,#7d8a60,#7a4630 55%,#6d7c4c)"></div>
  <h3>Cattle Name</h3>
  <p>Lorem ipsum dolor sit amet consectetur adipiscinges gravida. Risus commodo viverra maecenas accumsan lacus vel facilisis.</p>
  <div class="btn">View Sale</div>
</article>
<article class="card" style="left:449px">
  <div class="photo" role="img" aria-label="Black and tan highland cattle grazing together" style="background:linear-gradient(150deg,#3a3f2c,#2a2622 45%,#a08660 70%,#6f7c4c)"></div>
  <h3>Cattle Name</h3>
  <p>Lorem ipsum dolor sit amet consectetur adipiscinges gravida. Risus commodo viverra maecenas accumsan lacus vel facilisis.</p>
  <div class="btn">View Sale</div>
</article>
<article class="card" style="left:771px">
  <div class="photo" role="img" aria-label="Cream coloured highland calf grazing" style="background:linear-gradient(150deg,#3b3f2c,#e4dbc2 50%,#7b8756)"></div>
  <h3>Cattle Name</h3>
  <p>Lorem ipsum dolor sit amet consectetur adipiscinges gravida. Risus commodo viverra maecenas accumsan lacus vel facilisis.</p>
  <div class="btn">View Sale</div>
</article>
<div class="sdots"><span style="left:561px"></span><span style="left:583px"></span><span style="left:605px"></span><span style="left:627px"></span></div>

<section class="abs bulls"></section>
<div class="abs bulls-box"></div>
<div class="abs bulls-photo" role="img" aria-label="Black highland bull with wide horns behind a wire fence"></div>
<div class="bulls"><h2 class="abs display">OUR BULLS</h2></div>
<p class="abs bulls-text">Lorem ipsum dolor sit amet, conse ctetur adipiscing elit, sed do eiusmod tempor incididunt ut labore et dolore magna aliqua.</p>
<div class="abs outline-btn">Read More</div>

<section class="abs cows"></section>
<div class="cows"><h2 class="abs display center">COWS/HEIFERS</h2></div>
<p class="abs center cows-text">Lorem ipsum dolor sit amet, conse ctetur adipiscing elit, sed do<br>eiusmod tempor incididunt ut labore et dolore magna aliqua.</p>
<div class="btn" style="left:533px;top:3113px;width:132px;height:53px">Read More</div>
<div class="abs cows-photo" role="img" aria-label="Herd of white, tan and black cows standing in a dusty field"></div>

<section class="abs gallery"></section>
<div class="gallery"><h2 class="abs display center">GALLERY</h2></div>
<svg class="divider" style="left:508px;top:3629px" width="184" height="10"><line x1="0" y1="5" x2="184" y2="5" stroke="#55402a" stroke-width="2"/></svg>
<p class="abs center gallery-text">Lorem ipsum dolor sit amet, consectetur adipiscing elit, sed do eiusmod tempor<br>incididunt ut labore et dolore magna al suspendisse ultrices gravida.</p>
<div class="g" role="img" aria-label="Cream highland calf grazing" style="left:113px;top:3759px;width:314px;height:244px;background:linear-gradient(135deg,#4f5a34,#ddd2b6 55%,#6e7a48)"></div>
<div class="g" role="img" aria-label="Child standing beside a pale highland calf in a field" style="left:451px;top:3796px;width:312px;height:244px;background:linear-gradient(135deg,#9a9a80,#c9bfb2 50%,#85866a)"></div>
<div class="g" role="img" aria-label="Red highland cow in a pasture" style="left:788px;top:3767px;width:314px;height:244px;background:linear-gradient(135deg,#8a9a78,#7a3e22 55%,#6d7a4a)"></div>
<div class="g" role="img" aria-label="Ginger highland calf lit by evening sun" style="left:113px;top:4026px;width:314px;height:244px;background:linear-gradient(135deg,#6a6a3a,#c0622a 50%,#4e4a2a)"></div>
<div class="g" role="img" aria-label="Woman greeting a highland cow" style="left:451px;top:4063px;width:312px;height:244px;background:linear-gradient(135deg,#7a9a5a,#5a3a24 45%,#2a2622 70%,#6a8a4a)"></div>
<div class="g" role="img" aria-label="Black and tan highland cattle grazing side by side" style="left:788px;top:4036px;width:314px;height:294px;background:linear-gradient(135deg,#4a5a34,#1e1c1a 50%,#9a7a56 75%,#5a6a3a)"></div>
<div class="btn" style="left:533px;top:4385px;width:132px;height:53px">View More</div>

<svg class="abs" style="left:0;top:4498px" width="1200" height="14"><line x1="0" y1="7" x2="1200" y2="7" stroke="#4a4a4a" stroke-width="2"/></svg>

<h3 class="abs foot-h" style="left:226px;top:4617px">LINKS</h3>
<svg class="divider" style="left:226px;top:4655px" width="125" height="10"><line x1="0" y1="5" x2="125" y2="5" stroke="#3f2f1f" stroke-width="2"/></svg>
<nav class="foot-links">
  <a style="top:4694px">About</a>
  <a style="top:4725px">Cattle Sales</a>
  <a style="top:4756px">Bulls</a>
  <a style="top:4787px">Cows/Heifers</a>
  <a style="top:4818px">Gallery</a>
  <a style="top:4849px">Contact Us</a>
</nav>

<div class="abs" style="left:440px;top:4700px;width:320px;text-align:center">
  <div style="font-family:'Oswald',Arial,sans-serif;font-weight:500;font-size:36px;color:var(--brown);line-height:1">WRENFIELD CATTLE</div>
  <div style="font-family:'Oswald',Arial,sans-serif;font-weight:500;font-size:14px;color:var(--brown);margin-top:10px">HARLOW CREEK, CA</div>
</div>
<div class="social"><span style="left:524px"></span><span style="left:563px"></span><span style="left:602px"></span><span style="left:641px"></span></div>
<p class="abs center copyright">Copyright © 2025&nbsp; All Rights Reserved.</p>

<h3 class="abs foot-h" style="left:841px;top:4617px">CONTACT</h3>
<svg class="divider" style="left:841px;top:4655px" width="125" height="10"><line x1="0" y1="5" x2="125" y2="5" stroke="#3f2f1f" stroke-width="2"/></svg>
<div class="contact-item" style="top:4700px">
  <svg width="20" height="26" viewBox="0 0 24 30"><path fill="#3f2f1f" d="M12 0a10 10 0 0 0-10 10c0 7.5 10 20 10 20s10-12.5 10-20A10 10 0 0 0 12 0zm0 14a4 4 0 1 1 0-8 4 4 0 0 1 0 8z"/></svg>
  <div>Location:<br>Location Name 9785</div>
</div>
<div class="contact-item" style="top:4762px">
  <svg width="20" height="20" viewBox="0 0 24 24"><path fill="#3f2f1f" d="M6.6 10.8a15.2 15.2 0 0 0 6.6 6.6l2.2-2.2a1 1 0 0 1 1-.25 11.4 11.4 0 0 0 3.6.57 1 1 0 0 1 1 1V20a1 1 0 0 1-1 1A17 17 0 0 1 3 4a1 1 0 0 1 1-1h3.5a1 1 0 0 1 1 1c0 1.25.2 2.45.57 3.6a1 1 0 0 1-.25 1z"/></svg>
  <div>Phone:<br>5550 100200300</div>
</div>
<div class="contact-item" style="top:4823px">
  <svg width="22" height="18" viewBox="0 0 24 18"><path fill="#3f2f1f" d="M0 0h24v18H0zM2 2v1l10 7 10-7V2z"/></svg>
  <div style="text-transform:none">EMAIL:<br>INFO@WRENFIELD.EXAMPLE</div>
</div>

<div class="abs foot-photo" role="img" aria-label="Highland cattle feeding at hay racks in a misty field"></div>
</body>
</html>
```